[Raw Food + Juice Bar] Digital Menu Boards (2)

We need designs for our digital menu screens. Dimensions are 1080 x 1920 (9:16). Screens are in portrait mode–2 of them. They will be side by side so designs should be cohesive. We'll need the (Adobe) source files to be able to easily edit in the future.

Check out our Instagram (@pulpvia) to see current brand imagery for inspiration. Please disregard our current website design as it shows our old branding. Visit our Brightlistr page to get a feel of the store flow in which the menu boards will be displayed: https://www.brightlistr.com/biz/pulpvia-chicago-6

See "Larchmere Menu" attachment for content that will be incorporated into the design for 2 screens.

See "Cleanse Brochure" attachment to see current material we are using to promote our cleansing program. We would like to designate a portion of our menu to promote cleanse options, depending on how much room is available.

Also attached is a photo of our current, static menu board.

We've attached photos of color palettes we like.

Target Market(s)

Health-conscious individuals, healthy moms, fitness gurus, professionals

Industry/Entity Type

Health And Wellness

Font styles to use
Serif
Sans Serif

Colors

Designer to choose colors to be used in the design.

Requirements
Must have
• We need designs for our digital menu screens. Dimensions are 1080 x 1920 (9:16). Screens are in portrait mode–2 of them. We'll need the (Adobe) source files to be able to easily edit in the future. To ensure the sizing of the outputted file is correct and spaced correctly, send us a test file to test on our TV.
Nice to have
• Ideally, the menu will reflect current branding with font usage of one or more of the following:
• FuturaStd-Bold
• Desiderata-Regular
• Wisdom Script
• Bernier Typeface
• Swistblnk Banthers
• Hanley
• If there is space, we'd like to have space to roll a photo/video slideshow on the menu.

```html
<!DOCTYPE html>
<html lang="en">
<head>
<meta charset="utf-8">
<title>Pulpvia Smoothie Menu Board</title>
<link href="https://fonts.googleapis.com/css2?family=Anton&family=Fjalla+One&family=Kaushan+Script&family=Itim&display=swap" rel="stylesheet">
<style>
  :root {
    --board: #000000;
    --chalk: #ffffff;
    --lime: #bccd2b;
    --butter: #f6d862;
    --sketch: #262626;
    --rule: #d9d9d9;
  }
  * { margin: 0; padding: 0; box-sizing: border-box; }
  html, body { width: 675px; height: 1200px; overflow: hidden; background: var(--board); }
  .menu-board {
    position: relative; width: 675px; height: 1200px; background: var(--board);
    color: var(--chalk); font-family: "Itim", sans-serif; overflow: hidden;
  }
  .row { position: absolute; left: 0; right: 0; text-align: center; }
  .headline {
    top: 26px; font-family: "Anton", sans-serif; font-size: 52px; font-weight: 400; letter-spacing: 3px;
    line-height: 1; color: var(--chalk); text-shadow: 2px 2px 0 #555;
  }
  .headline-rule { position: absolute; top: 55px; height: 3px; width: 78px; background: var(--chalk); border-radius: 2px; }
  .headline-rule.left { left: 24px; }
  .headline-rule.right { right: 24px; }
  .section-title { top: 88px; font-family: "Kaushan Script", cursive; font-size: 42px; font-weight: 400; color: var(--lime); line-height: 1; }
  .size-tag {
    display: inline-block; font-family: "Fjalla One", sans-serif; font-size: 15px; color: var(--lime);
    border: 2px solid var(--lime); border-radius: 6px; padding: 0 4px; vertical-align: 14px; margin-left: 10px;
  }
  .item-name { font-family: "Fjalla One", sans-serif; font-size: 23px; font-weight: 400; color: var(--lime); line-height: 1; letter-spacing: .5px; }
  .item-name .price { color: var(--chalk); font-size: 18px; margin-left: 8px; }
  .item-name .note { font-size: 12px; margin-left: 8px; vertical-align: 3px; }
  .ingredients { font-size: 15.5px; line-height: 18px; }
  .ingredients.loose { line-height: 23px; }
  .ingredients .step { color: var(--lime); }
  .divider { left: 210px; right: 210px; height: 5px; border-top: 1.5px solid var(--rule); border-bottom: 1.5px solid var(--rule); position: absolute; }
  .sketch { position: absolute; background: var(--sketch); border-radius: 40%; }
  .flourish { position: absolute; top: 938px; left: 210px; width: 256px; height: 22px; background: var(--butter); opacity: .85; border-radius: 11px; }
  .cleanse-title {
    top: 970px; font-family: "Anton", sans-serif; font-size: 35px; font-weight: 400; letter-spacing: 2px; color: var(--butter); line-height: 1;
    text-shadow: 2px 2px 0 #6b5a1f;
  }
  .cleanse-copy { font-family: "Fjalla One", sans-serif; font-size: 18.5px; line-height: 27px; letter-spacing: .8px; }
</style>
</head>
<body>
<main class="menu-board">
  <span class="headline-rule left"></span>
  <span class="headline-rule right"></span>
  <h1 class="row headline">PURVEYORS OF PURE</h1>
  <h2 class="row section-title">Smoothies <span class="size-tag">18oz</span></h2>

  <div class="sketch" role="img" aria-label="Chalk sketch of almonds" style="left:32px;top:216px;width:100px;height:60px"></div>
  <div class="sketch" role="img" aria-label="Chalk sketch of dates" style="left:552px;top:224px;width:100px;height:52px"></div>
  <div class="sketch" role="img" aria-label="Chalk sketch of leeks" style="left:32px;top:288px;width:112px;height:60px"></div>
  <div class="sketch" role="img" aria-label="Chalk sketch of a halved avocado" style="left:32px;top:520px;width:80px;height:100px"></div>
  <div class="sketch" role="img" aria-label="Chalk sketch of a pineapple" style="left:570px;top:480px;width:70px;height:128px"></div>
  <div class="sketch" role="img" aria-label="Chalk sketch of broccoli" style="left:24px;top:672px;width:70px;height:72px"></div>
  <div class="sketch" role="img" aria-label="Chalk sketch of bananas" style="left:566px;top:772px;width:74px;height:72px"></div>

  <h3 class="row item-name" style="top:152px">NIGHT EMBER<span class="price">10.5</span></h3>
  <p class="row ingredients" style="top:183px">Housemade Almond Milk, Cold Brew Coffee, Banana, Coconut Meat, Raw Cacao,<br>Medjool Dates, Tocotrienols, Maca<br>Topped with Raw Cacao Drizzle and Housemade Coconut Whip</p>
  <span class="divider" style="top:245px"></span>

  <h3 class="row item-name" style="top:258px">JADE BLOSSOM<span class="price">11</span></h3>
  <p class="row ingredients" style="top:288px">Housemade Almond Milk, Banana, Avocado, Spinach, Sprouted Almond Butter,<br>Verdura Greens, Maca, Moringa, Medjool Dates, Tocotrienols</p>
  <span class="divider" style="top:331px"></span>

  <h3 class="row item-name" style="top:344px">EMERALD GALA<span class="price">10</span></h3>
  <p class="row ingredients" style="top:373px">Housemade Almond Milk, Banana, Avocado, Pineapple, Spinach, Matcha, Spirulina, Mint,<br>Tocotrienols, Local Honey, Pink Salt (Upgrade: Verdura Greens, +1)</p>
  <span class="divider" style="top:415px"></span>

  <h3 class="row item-name" style="top:429px">OLD ORCHARD WAY<span class="price">10</span></h3>
  <p class="row ingredients" style="top:458px">Housemade Almond Milk, Banana, Blueberries, Peanut Butter, Medjool Dates,<br>Tocotrienols, Lucuma, Pink Salt</p>
  <span class="divider" style="top:501px"></span>

  <h3 class="row item-name" style="top:516px">MACA POWER UP<span class="price">10.5</span></h3>
  <p class="row ingredients loose" style="top:543px">Fresh-cracked Coconut Water, Cherries, Banana, Peanut Butter,<br>Vegan Mocha Protein Powder, Maca</p>
  <span class="divider" style="top:593px"></span>

  <h3 class="row item-name" style="top:606px">EMBER SQUAD<span class="price">10</span></h3>
  <p class="row ingredients loose" style="top:634px">Fresh-cracked Coconut Water, Apple Juice, Coconut Meat, Banana, Mango, Pineapple,<br>Strawberry, Tocotrienols, Camu Camu, Hemp Seeds, Jalapeno</p>
  <span class="divider" style="top:683px"></span>

  <h3 class="row item-name" style="top:698px">FROST MINT<span class="price">10.5</span><span class="note">*SEASONAL*</span></h3>
  <p class="row ingredients" style="top:727px">Almond Milk, Banana, Cherries, Raw Cacao Drizzle, Sprouted Almond Butter,<br>Tocotrienols, Dates, Peppermint, Pink Salt<br>Topped with Raw Cacao Drizzle, Cacao Nibs, Mint and Housemade Coconut Whip</p>
  <span class="divider" style="top:789px"></span>

  <h3 class="row item-name" style="top:803px">BUILD YOUR OWN SMOOTHIE<span class="price">10.5</span></h3>
  <p class="row ingredients" style="top:833px"><span class="step">STEP 1:</span> Start with Your Liquid: Housemade Almond Milk, Apple Juice,<br>or Coconut Water <span class="step">+ STEP 2:</span> Add Your Base: Avocado, Banana, or Coconut Meat<br><span class="step">+ STEP 3:</span> Choose up to 3 Fruits/ Veggies <span class="step">+ STEP 4:</span> Choose up to 2 Superfoods<br><span class="step">+ STEP 5:</span> Choose a Sweetener (Medjool Dates, Local Honey, Xylitol)</p>

  <div class="flourish" role="img" aria-label="Yellow swoosh ornament"></div>

  <h2 class="row cleanse-title">SIGNATURE JUICE &amp; SMOOTHIE CLEANSES</h2>
  <p class="row cleanse-copy" style="top:1020px">AVAILABLE AT 65/DAY WITH NATIONWIDE DELIVERY AVAILABLE.</p>
  <p class="row cleanse-copy" style="top:1060px">CHOOSE FROM 5 DIFFERENT SIGNATURE CLEANSES<br>AVAILABLE IN 1, 3, 5 OR 7 DAY PACKAGES.</p>
  <p class="row cleanse-copy" style="top:1128px">REBOOT YOUR BODY BY PROVIDING A DIGESTIVE VACATION<br>WHILE REFOCUSING THE MIND.</p>
</main>
</body>
</html>
```